M25 Billboard Advert Required Please

I need an advert for a motorway Billboard on the M25 , the advert should show the following in big letters:
GUTTER CLEANING
DALRYNFLUES.COM and a small logo off to the side (Our logo is attached)

The printer has requested the following (Important please) the advert has to be
pdf file / 300 dpi/landscape orientation / scaled to a minimum 25% advert size ( this particular site is 22ft x 10ft so 25% of this please). Please also make sure that the artwork is embedded and outlined correctly if this is incorrect it will affect the printing of the banner.

Target Market(s)

General Public

Industry/Entity Type

Gutter Cleaning

Requirements
Should not have
• No Change to our Logo

```html
<!DOCTYPE html>
<html lang="en">
<head>
<meta charset="utf-8">
<title>Dalryn Flues – Gutter Cleaning Billboard</title>
<link rel="stylesheet" href="https://fonts.googleapis.com/css2?family=Montserrat:wght@800&family=Oswald:wght@500&family=Open+Sans:wght@600&display=swap">
<style>
  :root {
    --page-bg: #f6f4f4;
    --ink: #111111;
    --panel-white: #ffffff;
    --panel-grey: #eceded;
    --brand-red: #8f141a;
    --brand-red-dark: #6e0d12;
    --band-black: #050505;
    --text-white: #ffffff;
    --tagline: #2a2a2a;
    --roof-green: #5d7a70;
    --roof-dark: #2d2f30;
    --gutter-light: #b9b8ae;
    --gutter-dark: #4b4a42;
  }
  html, body {
    margin: 0;
    padding: 0;
    width: 1050px;
    height: 1200px;
    overflow: hidden;
    background: var(--page-bg);
  }
  .canvas {
    position: relative;
    width: 1050px;
    height: 1200px;
  }
  .billboard {
    position: absolute;
    left: 30px;
    top: 375px;
    width: 990px;
    height: 451px;
    display: block;
  }
  .brand-name {
    font-family: 'Montserrat', sans-serif;
    font-weight: 800;
    fill: var(--ink);
  }
  .tagline {
    font-family: 'Open Sans', sans-serif;
    font-weight: 600;
    fill: var(--tagline);
  }
  .headline {
    font-family: 'Montserrat', sans-serif;
    font-weight: 800;
    fill: var(--text-white);
  }
  .web-address {
    font-family: 'Oswald', sans-serif;
    font-weight: 500;
    fill: var(--text-white);
  }
</style>
</head>
<body>
<main class="canvas">
  <svg class="billboard" viewBox="0 0 1690 770" xmlns="http://www.w3.org/2000/svg" aria-labelledby="billboard-title">
    <title id="billboard-title">Dalryn Flues gutter cleaning billboard</title>
    <defs>
      <linearGradient id="panel-fade" x1="0" y1="0" x2="1" y2="1">
        <stop offset="0" stop-color="var(--panel-grey)"/>
        <stop offset="0.6" stop-color="var(--panel-white)"/>
      </linearGradient>
      <linearGradient id="red-fade" x1="0" y1="0" x2="1" y2="0">
        <stop offset="0" stop-color="var(--brand-red)"/>
        <stop offset="1" stop-color="var(--brand-red-dark)"/>
      </linearGradient>
      <linearGradient id="roof-tones" x1="0" y1="0" x2="1" y2="0">
        <stop offset="0" stop-color="var(--roof-green)"/>
        <stop offset="0.5" stop-color="var(--roof-dark)"/>
        <stop offset="1" stop-color="#555a5c"/>
      </linearGradient>
      <linearGradient id="gutter-tones" x1="0" y1="0" x2="0" y2="1">
        <stop offset="0" stop-color="var(--roof-dark)"/>
        <stop offset="0.25" stop-color="var(--gutter-light)"/>
        <stop offset="0.8" stop-color="var(--gutter-dark)"/>
        <stop offset="1" stop-color="#1c1c1a"/>
      </linearGradient>
    </defs>

    <!-- brand panel -->
    <rect class="brand-panel" x="0" y="0" width="1690" height="770" fill="url(#panel-fade)"/>

    <!-- roof photo area -->
    <polygon class="photo-frame" points="1055,0 1690,0 1690,380 870,380" fill="var(--band-black)"/>
    <polygon class="photo-roof" role="img" aria-label="Photo of a worker in gloves kneeling on a roof clearing a gutter"
             points="1095,25 1690,25 1690,380 915,380" fill="url(#roof-tones)"/>

    <!-- red strip above headline -->
    <polygon class="red-strip" points="0,345 890,345 872,380 0,380" fill="url(#red-fade)"/>

    <!-- headline band -->
    <rect class="headline-band" x="0" y="380" width="1690" height="185" fill="var(--band-black)"/>
    <text class="headline" x="62" y="535" font-size="150" textLength="1560" lengthAdjust="spacingAndGlyphs">GUTTER CLEANING</text>

    <!-- gutter photo area -->
    <polygon class="photo-gutter" role="img" aria-label="Photo of a mossy gutter full of leaves"
             points="832,565 1690,565 1690,770 722,770" fill="url(#gutter-tones)"/>
    <polygon class="divider" points="795,565 832,565 722,770 695,770" fill="var(--panel-white)"/>

    <!-- web address block -->
    <polygon class="address-block" points="0,565 795,565 695,770 0,770" fill="url(#red-fade)"/>
    <text class="web-address" x="45" y="697" font-size="128" textLength="655" lengthAdjust="spacingAndGlyphs">DALRYNFLUES.COM</text>

    <!-- brand -->
    <rect class="brand-mark" x="100" y="100" width="80" height="80" fill="var(--brand-red)"/>
    <text class="brand-name" x="210" y="178" font-size="96" textLength="600" lengthAdjust="spacingAndGlyphs">Dalryn Flues</text>
    <text class="tagline" x="97" y="275" font-size="44" textLength="713" lengthAdjust="spacingAndGlyphs">Clean gutters protect your property</text>
  </svg>
</main>
</body>
</html>
```